Kentucky residential recovery center needs a flyer design

We need a flyer design for a 16 bed male residential/inpatient recovery center based in Richmond, Kentucky. The facility provides short term (average 30 day) treatment to those struggling with substace abuse and addiction. The design should communicate trust, assurance, safety.
Our wesite provides more information https://morvalcare.org/treatment-services/residential-treatment/

Target Market(s)

Men (typically 30-50) struggling with substance addiction

```html
<!DOCTYPE html>
<html lang="en">
<head>
<meta charset="utf-8">
<title>Morval Care – Residential/Inpatient Recovery Center Flyer</title>
<link rel="stylesheet" href="https://fonts.googleapis.com/css2?family=Oswald:wght@400;500&family=Poppins:wght@400;500;600;700;800;900&display=swap">
<style>
  :root{
    --blue:#2a5d8d;
    --navy:#1b2a8f;
    --ink:#1c2670;
    --sky:#62b2ec;
    --link:#3a6fc4;
    --pale:#d3e9fa;
    --green:#23a134;
    --green-light:#a6e0ab;
    --white:#ffffff;
    --text:#1d1d2b;
    --stage:#eef0f3;
  }
  *{margin:0;padding:0;box-sizing:border-box}
  html,body{width:820px;height:1200px;overflow:hidden;background:var(--stage)}
  body{position:relative;font-family:"Poppins",sans-serif;color:var(--text)}
  ul,ol{list-style:none}

  .sheet{position:absolute;left:185px;width:450px;height:582px;box-shadow:0 6px 18px rgba(0,0,0,.18);background:var(--white)}
  .sheet-front{top:12px}
  .sheet-back{top:606px}
  .page{position:relative;width:600px;height:776px;overflow:hidden;transform:scale(.75);transform-origin:0 0;background:var(--white)}
  .backdrop{position:absolute;inset:0}
  .abs{position:absolute}

  /* ---------- front page ---------- */
  .brand{left:62px;top:28px;width:106px;height:106px;border-radius:50%;border:2px solid var(--navy);display:flex;align-items:center;justify-content:center}
  .brand-name{font-weight:700;font-size:14px;color:var(--navy);letter-spacing:1px;text-align:center;line-height:1.15}

  .headline{left:36px;top:156px}
  .headline-kicker{display:block;font-family:"Oswald",sans-serif;font-weight:500;font-size:30px;color:var(--white);line-height:1.05;letter-spacing:-.3px}
  .headline-main{display:block;font-weight:800;font-size:50px;color:var(--sky);line-height:.92;letter-spacing:-.5px;margin-top:2px}
  .headline-note{margin-top:8px;border-left:3px solid var(--sky);padding-left:10px;color:var(--white);font-size:10.5px;line-height:1.3;width:270px}

  .photo-ring{left:322px;top:40px;width:276px;height:276px;border-radius:50%;background:var(--navy)}
  .photo{left:338px;top:56px;width:248px;height:248px;border-radius:50%;background:radial-gradient(circle at 40% 45%,#b59c7c 0%,#8a7560 45%,#4a4a58 100%)}
  .location-badge{left:302px;top:226px;width:138px;height:138px;border-radius:50%;background:var(--navy);border:4px solid var(--blue);display:flex;flex-direction:column;align-items:center;justify-content:center;font-family:"Oswald",sans-serif;line-height:1}
  .location-badge .based{color:var(--white);font-size:17px;letter-spacing:4px;font-weight:500}
  .location-badge .city{color:var(--sky);font-size:25px;font-weight:400;margin-top:4px}
  .location-badge .city + .city{margin-top:2px}

  .problems-tag{left:0;top:406px;width:170px;height:20px;background:var(--sky);border-radius:0 3px 3px 0;font-size:7.5px;font-weight:700;color:var(--ink);display:flex;align-items:center;justify-content:center}
  .issues-title{left:188px;top:372px;line-height:1}
  .issues-title .a{font-family:"Oswald",sans-serif;font-size:17px;color:var(--navy);font-weight:500}
  .issues-title .b{font-weight:800;font-size:19px;color:var(--navy);line-height:1}
  .issues-title .c{font-weight:800;font-size:20px;color:var(--green);line-height:1.05}
  .issues-divider{left:422px;top:370px;width:1.5px;height:62px;background:#cfd6e6}
  .issue{position:absolute;display:flex;align-items:center;gap:6px;font-size:8.5px;font-weight:700;color:var(--ink);line-height:1.05}
  .issue svg{flex:none}

  .why{left:30px;top:442px;width:538px;height:135px;background:var(--green);border-radius:9px;border-top:7px solid var(--navy)}
  .why-tab{left:228px;top:442px;width:144px;height:22px;background:var(--navy);border-radius:0 0 10px 10px;color:var(--white);font-weight:700;font-size:10.5px;display:flex;align-items:center;justify-content:center}
  .stat{position:absolute;top:476px}
  .stat-head{height:56px;font-family:"Oswald",sans-serif;font-weight:400;color:var(--navy);font-size:13.5px;line-height:1.05;text-transform:uppercase}
  .stat-head .big{font-size:21px;display:block;line-height:1.05}
  .stat-body{color:var(--white);font-size:8px;line-height:1.25}
  .stat-rule{position:absolute;top:478px;width:1px;height:88px;background:rgba(255,255,255,.45)}

  .facility{left:20px;top:584px;width:560px;text-align:center;font-weight:700;font-size:10.5px;line-height:1.3}
  .how-title{left:36px;top:616px;font-weight:700;font-size:11px;color:var(--navy)}
  .how-title span{color:var(--green)}
  .step{position:absolute;top:634px;width:142px;height:86px;background:var(--pale);padding:10px 8px 6px 26px;font-size:8px;line-height:1.3}
  .step-icon{position:absolute;left:-22px;top:23px;width:40px;height:40px;border-radius:50%;background:var(--white);border:2.5px solid var(--sky);display:flex;align-items:center;justify-content:center}

  .contact{top:728px;display:flex;align-items:center;font-size:8.5px}
  .contact .cta{font-weight:700;font-size:11px;color:var(--navy)}
  .contact .cta span{color:var(--green)}
  .contact-item{position:absolute;display:flex;align-items:center;gap:5px;font-size:8.5px;color:var(--text)}

  /* ---------- back page ---------- */
  .programs-title{left:37px;top:34px;line-height:.98;font-weight:900;font-size:40px;letter-spacing:-.3px}
  .programs-title .a{display:block;color:var(--green)}
  .programs-title .b{display:block;color:var(--white)}
  .programs-copy{left:37px;top:122px;width:282px;color:var(--white);font-size:7.6px;line-height:1.3}
  .programs-copy p + p{margin-top:9px}
  .program{position:absolute;display:flex;align-items:flex-start;gap:6px;color:var(--white);font-weight:700;font-size:9.5px;line-height:1.2}

  .hero-ring{left:320px;top:25px;width:280px;height:280px;border-radius:50%;background:var(--green)}
  .hero-photo{left:332px;top:37px;width:256px;height:256px;border-radius:50%;background:radial-gradient(circle at 50% 55%,#9c7b55 0%,#6e5a48 45%,#3b3a40 100%)}
  .sub-photo{border-radius:50%;border:4px solid var(--white)}
  .sub-photo-a{left:321px;top:200px;width:126px;height:126px;background:radial-gradient(circle at 50% 60%,#6f6f76 0%,#3c3d45 70%)}
  .sub-photo-b{left:438px;top:238px;width:112px;height:112px;background:radial-gradient(circle at 50% 45%,#a7b3c3 0%,#6a5c52 70%)}

  .works-title{left:0;top:356px;width:600px;text-align:center;font-weight:700;font-size:12.5px;color:var(--green)}
  .works-lede{left:0;top:380px;width:600px;text-align:center;font-weight:700;font-size:10px;line-height:1.3;color:var(--text)}
  .feature{position:absolute}
  .feature-icon{position:absolute;width:36px;height:36px;border-radius:50%;background:var(--navy);display:flex;align-items:center;justify-content:center}
  .feature-title{font-size:8.3px;font-weight:600;color:var(--sky);text-transform:uppercase;line-height:1.2}
  .feature-body{font-size:7.3px;line-height:1.3;color:var(--text);margin-top:2px}
  .works-divider{left:300px;top:420px;width:1.5px;height:190px;background:var(--navy)}

  .quote{left:27px;top:569px;width:265px;height:80px;background:var(--sky);border-radius:12px;padding:10px 14px 6px 12px;color:var(--white);font-size:7.3px;line-height:1.3}
  .quote cite{display:block;text-align:right;font-style:normal;font-weight:700;color:var(--ink);margin-right:36px}
  .quote-mark{font-family:"Poppins",sans-serif;font-weight:900;font-size:42px;line-height:1;color:var(--sky)}

  .person{left:540px;top:568px;width:60px;height:208px;border-radius:28px 0 0 0;background:linear-gradient(180deg,#8d9099 0%,#6f737c 55%,#d48a86 80%,#c57a78 100%)}

  .insurers-title{left:37px;top:680px;font-weight:700;font-size:11.5px;color:var(--green)}
  .insurers{left:37px;top:704px;width:230px;display:grid;grid-template-columns:repeat(4,1fr);gap:7px 8px}
  .insurer{height:13px;border-radius:3px}

  .transport{left:307px;top:644px;font-weight:700;font-size:7.6px;color:var(--navy)}
  .site{position:absolute;left:307px;display:flex;gap:6px;align-items:flex-start}
  .site-name{font-family:"Oswald",sans-serif;font-size:10.5px;color:var(--link);line-height:1.1}
  .site-address{font-size:7.6px;line-height:1.3;color:var(--text)}
</style>
</head>
<body>

<!-- FRONT -->
<section class="sheet sheet-front">
<div class="page">
  <svg class="backdrop" width="600" height="776" viewBox="0 0 600 776" aria-hidden="true">
    <rect width="600" height="460" fill="var(--blue)"/>
    <path d="M0 0 H265 C222 78 130 130 0 142 Z" fill="var(--white)"/>
    <path d="M265 0 C222 78 130 130 0 142" fill="none" stroke="var(--green)" stroke-width="4"/>
    <path d="M0 420 C120 398 170 364 300 335 C420 308 520 298 600 290" fill="none" stroke="var(--green-light)" stroke-width="8"/>
    <path d="M0 432 C120 410 170 375 300 346 C420 320 520 309 600 301 V776 H0 Z" fill="var(--white)"/>
    <path d="M0 432 C120 410 170 375 300 346 C420 320 520 309 600 301" fill="none" stroke="var(--green)" stroke-width="5"/>
  </svg>

  <div class="abs brand"><p class="brand-name">MORVAL<br>CARE</p></div>

  <div class="abs photo-ring"></div>
  <div class="abs photo" role="img" aria-label="Photo of a residential bedroom with a bunk bed, sofa and wooden floor"></div>
  <div class="abs location-badge">
    <span class="based">BASED IN</span>
    <span class="city">RICHMOND</span>
    <span class="city">KENTUCKY</span>
  </div>

  <header class="abs headline">
    <h1>
      <span class="headline-kicker">RESIDENTIAL/INPATIENT</span>
      <span class="headline-main">RECOVERY<br>CENTER</span>
    </h1>
    <p class="headline-note">The program has a small capacity of 16 men, split into two groups of 8. This ensures treatment is individualised.</p>
  </header>

  <div class="abs problems-tag">PROBLEMS WE CAN HELP WITH</div>

  <h2 class="abs issues-title"><span class="a">WHAT ISSUES</span><br><span class="b">CAN BE</span><br><span class="c">TREATED?</span></h2>
  <div class="abs issues-divider"></div>
  <ul>
    <li class="issue" style="left:314px;top:368px">
      <svg width="18" height="24" viewBox="0 0 24 32"><rect x="9" y="1" width="6" height="7" fill="var(--green)"/><rect x="5" y="8" width="14" height="23" rx="3" fill="var(--green)"/><rect x="8" y="15" width="8" height="8" fill="#fff"/></svg>
      ALCOHOLISM</li>
    <li class="issue" style="left:431px;top:368px">
      <svg width="24" height="24" viewBox="0 0 32 32"><path d="M6 26 L22 10" stroke="var(--green)" stroke-width="6"/><path d="M4 28 L8 24" stroke="var(--green)" stroke-width="2"/><path d="M20 6 L26 12 M24 4 L28 8" stroke="var(--green)" stroke-width="3"/></svg>
      DRUG ADDICTION</li>
    <li class="issue" style="left:314px;top:406px">
      <svg width="18" height="22" viewBox="0 0 24 30"><rect x="3" y="1" width="18" height="6" fill="var(--green)"/><rect x="2" y="8" width="20" height="21" rx="2" fill="var(--green)"/><path d="M12 13 V24 M6.5 18.5 H17.5" stroke="#fff" stroke-width="3"/></svg>
      MEDICATION<br>ADDICTION</li>
    <li class="issue" style="left:431px;top:404px">
      <svg width="22" height="22" viewBox="0 0 30 30"><circle cx="11" cy="8" r="6" fill="var(--green)"/><path d="M1 29 C1 18 21 18 21 29 Z" fill="var(--green)"/><circle cx="23" cy="21" r="5" fill="none" stroke="var(--green)" stroke-width="2.5"/></svg>
      BEHAVIORAL<br>HEALTH</li>
  </ul>

  <section>
    <div class="abs why"></div>
    <h2 class="abs why-tab">WHY CHOOSE US?</h2>
    <div class="stat" style="left:45px;width:100px"><p class="stat-head"><span class="big">100+</span>Years</p><p class="stat-body">Over 100 years of medical and clinical experience behind our team</p></div>
    <div class="stat-rule" style="left:154px"></div>
    <div class="stat" style="left:168px;width:104px"><p class="stat-head"><span class="big">95%</span>Satisfaction<br>rating</p><p class="stat-body">Our patients rate us 95 out of 100.</p></div>
    <div class="stat-rule" style="left:280px"></div>
    <div class="stat" style="left:292px;width:120px"><p class="stat-head"><span class="big">#1</span>Best drug &amp; alcohol<br>rehab center</p><p class="stat-body">Voted one of the best Alcohol and Drug rehab centers</p></div>
    <div class="stat-rule" style="left:420px"></div>
    <div class="stat" style="left:432px;width:126px"><p class="stat-head"><span class="big">2,500+</span>Patients treated</p><p class="stat-body">Over 2,500 patients treated successfully and counting.</p></div>
  </section>

  <p class="abs facility">THE FACILITY PROVIDES SHORT TERM (AVERAGE 30 DAY) TREATMENT TO THOSE<br>STRUGGLING WITH SUBSTANCE ABUSE AND ADDICTION.</p>

  <h2 class="abs how-title">HOW DOES <span>IT WORK?</span></h2>
  <ol>
    <li class="step" style="left:58px">
      <span class="step-icon"><svg width="20" height="19" viewBox="0 0 26 24"><path d="M2 2 H18 V14 H8 L3 18 V14 H2 Z" fill="var(--navy)"/><path d="M20 7 H24 V19 H23 V23 L19 19 H10 V16 H20 Z" fill="var(--sky)"/></svg></span>
      Speak with our team in private about the nature of your challenges and what you need help with</li>
    <li class="step" style="left:238px">
      <span class="step-icon"><svg width="17" height="20" viewBox="0 0 22 26"><circle cx="11" cy="7" r="6" fill="var(--navy)"/><path d="M1 26 C1 14 21 14 21 26 Z" fill="var(--navy)"/><path d="M11 17 V24 M7.5 20.5 H14.5" stroke="#fff" stroke-width="2"/></svg></span>
      Together we select an appropriate time slot to book you in for an induction appointment with one of our clinical staff</li>
    <li class="step" style="left:418px">
      <span class="step-icon"><svg width="22" height="22" viewBox="0 0 28 28"><circle cx="14" cy="14" r="12" fill="none" stroke="var(--navy)" stroke-width="2.5"/><path d="M11 8 L20 14 L11 20 Z" fill="var(--navy)"/></svg></span>
      Once the induction is completed, we'll schedule you in to commence your inpatient program</li>
  </ol>

  <footer>
    <p class="abs contact cta" style="left:36px">GET IN TOUCH WITH US NOW.&nbsp;<span>WE'RE HERE TO HELP!</span></p>
    <p class="contact-item" style="left:361px;top:730px"><svg width="10" height="10" viewBox="0 0 14 14"><circle cx="7" cy="7" r="7" fill="var(--navy)"/><path d="M4.5 3.5 L6 5.5 L5.2 6.5 C5.8 7.7 6.5 8.4 7.5 8.8 L8.5 8 L10.5 9.5 L9.7 10.7 C7 10.5 3.6 7 3.3 4.3 Z" fill="#fff"/></svg>859-555-0142</p>
    <p class="contact-item" style="left:457px;top:730px"><svg width="10" height="10" viewBox="0 0 14 14"><circle cx="7" cy="7" r="6" fill="none" stroke="var(--navy)" stroke-width="2"/><path d="M1 7 H13 M7 1 C4 4 4 10 7 13 M7 1 C10 4 10 10 7 13" fill="none" stroke="var(--navy)" stroke-width="1.2"/></svg>morvalcare.org</p>
  </footer>
</div>
</section>

<!-- BACK -->
<section class="sheet sheet-back">
<div class="page">
  <svg class="backdrop" width="600" height="776" viewBox="0 0 600 776" aria-hidden="true">
    <rect width="600" height="420" fill="var(--blue)"/>
    <path d="M0 382 C150 350 300 326 600 282" fill="none" stroke="var(--green-light)" stroke-width="8"/>
    <path d="M0 394 C150 362 300 338 600 293 V776 H0 Z" fill="var(--white)"/>
    <path d="M0 394 C150 362 300 338 600 293" fill="none" stroke="var(--green)" stroke-width="5"/>
  </svg>

  <div class="abs hero-ring"></div>
  <div class="abs hero-photo" role="img" aria-label="Photo of a lounge with leather sofas and a coffee table"></div>
  <div class="abs sub-photo sub-photo-a" role="img" aria-label="Photo of a meeting room with a round table and chairs"></div>
  <div class="abs sub-photo sub-photo-b" role="img" aria-label="Photo of a living room with a rug and television"></div>

  <h1 class="abs programs-title"><span class="a">TREATMENT</span><span class="b">PROGRAMS</span></h1>
  <div class="abs programs-copy">
    <p>We provide three personalized treatment options for individuals struggling with addiction.</p>
    <p>Our treatment philosophy is to treat clients with the lowest dose of Medication Assisted Therapy ('MAT') to remove their cravings and withdrawals so that they may begin their path of rehabilitation without the physical obstacles to recovery.</p>
    <p>We believe clients can successfully taper off 'MAT' after acquiring the support and skills they need to obtain their goal of sobriety.</p>
  </div>
  <ul>
    <li class="program" style="left:37px;top:252px"><svg width="10" height="10" viewBox="0 0 10 10"><circle cx="5" cy="5" r="5" fill="var(--sky)"/><path d="M2.6 5.2 L4.3 6.8 L7.4 3.6" fill="none" stroke="#fff" stroke-width="1.4"/></svg>INPATIENT/<br>RESIDENTIAL</li>
    <li class="program" style="left:152px;top:252px"><svg width="10" height="10" viewBox="0 0 10 10"><circle cx="5" cy="5" r="5" fill="var(--sky)"/><path d="M2.6 5.2 L4.3 6.8 L7.4 3.6" fill="none" stroke="#fff" stroke-width="1.4"/></svg>INTENSIVE OUTPATIENT<br>PROGRAM (IOP)</li>
    <li class="program" style="left:37px;top:290px"><svg width="10" height="10" viewBox="0 0 10 10"><circle cx="5" cy="5" r="5" fill="var(--sky)"/><path d="M2.6 5.2 L4.3 6.8 L7.4 3.6" fill="none" stroke="#fff" stroke-width="1.4"/></svg>OUTPATIENT</li>
  </ul>

  <h2 class="abs works-title">WHY TREATMENT HERE WORKS</h2>
  <p class="abs works-lede">We treat patients the way we would want to be treated which is illustrated<br>by our 95% satisfaction rate from our patients.</p>
  <div class="abs works-divider"></div>

  <div class="feature" style="left:37px;top:421px;width:240px">
    <span class="feature-icon" style="left:0;top:4px"><svg width="18" height="18" viewBox="0 0 18 18"><path d="M9 2 C12 6 14 8 14 11 A5 5 0 0 1 4 11 C4 8 6 6 9 2 Z" fill="#fff"/></svg></span>
    <div style="margin-left:42px"><h3 class="feature-title">Evidence based treatment</h3><p class="feature-body">We use evidence-based treatment that has been scientifically tested and proven to produce positive results. Ranging from cognitive behaviour therapy to dialectical therapy, we do what it takes to make you healthy.</p></div>
  </div>
  <div class="feature" style="left:37px;top:504px;width:240px">
    <span class="feature-icon" style="left:0;top:4px"><svg width="14" height="18" viewBox="0 0 14 18"><rect x="1" y="1" width="12" height="16" rx="2" fill="none" stroke="#fff" stroke-width="1.6"/><path d="M4 9 H10 M7 6 V12" stroke="#fff" stroke-width="1.6"/></svg></span>
    <div style="margin-left:42px"><h3 class="feature-title">Telemedicine</h3><p class="feature-body">Morval Care is offering aspects of its treatment program via telehealth services to meet the need of clients seeking treatment from the convenience of their homes.</p></div>
  </div>
  <div class="feature" style="left:312px;top:421px;width:252px">
    <span class="feature-icon" style="left:0;top:4px"><svg width="18" height="18" viewBox="0 0 18 18"><circle cx="8" cy="6" r="3.5" fill="none" stroke="#fff" stroke-width="1.6"/><path d="M2 16 C2 10 14 10 14 16" fill="none" stroke="#fff" stroke-width="1.6"/><path d="M11 13 L13 15 L17 11" fill="none" stroke="#fff" stroke-width="1.6"/></svg></span>
    <div style="margin-left:44px"><h3 class="feature-title">Individualized</h3><p class="feature-body">You deserve individualized attention from experienced professionals who actually care. Our reputation, small case load and success rates mean you are given the best treatment from leading experts.</p></div>
  </div>
  <div class="feature" style="left:312px;top:504px;width:228px">
    <span class="feature-icon" style="left:0;top:4px"><svg width="18" height="16" viewBox="0 0 18 16"><circle cx="5" cy="5" r="2.5" fill="#fff"/><circle cx="13" cy="5" r="2.5" fill="#fff"/><path d="M1 15 C1 9 9 9 9 15 M9 15 C9 9 17 9 17 15" fill="#fff"/></svg></span>
    <div style="margin-left:44px"><h3 class="feature-title">Medication assisted treatment</h3><p class="feature-body">Medication assisted treatment helps to relieve withdrawal symptoms and cravings which makes going clean easier. We treat addiction with FDA-approved medicines to help you focus on your recovery. We prescribe medicines such as Subrelia (a treatment combining buprenorphine and naloxone), Naltravia (a naltrexone treatment), and Bupracade (a buprenorphine treatment)</p></div>
  </div>

  <span class="abs quote-mark" style="left:34px;top:540px">&ldquo;</span>
  <blockquote class="abs quote">
    <p>Great people, they changed my life in so many ways. Mark stopped his daily life to come to court with me out of a bad spot. they're not just a doc office, they're people who want to make a difference. I love u all thanks for the help you have given me.</p>
    <cite>– DALE M</cite>
  </blockquote>
  <span class="abs quote-mark" style="left:248px;top:632px">&rdquo;</span>

  <div class="abs person" role="img" aria-label="Photo of a smiling client holding a program completion certificate"></div>

  <h2 class="abs insurers-title">MOST INSURANCES ACCEPTED</h2>
  <div class="abs insurers" role="img" aria-label="Accepted insurance provider badges">
    <span class="insurer" style="background:#8fb8d8"></span>
    <span class="insurer" style="background:#9fcf8a"></span>
    <span class="insurer" style="background:#8a9bc8"></span>
    <span class="insurer" style="background:#9ab3dd"></span>
    <span class="insurer" style="background:#c9a2c8"></span>
    <span class="insurer" style="background:#b8bcc4"></span>
    <span class="insurer" style="background:#8fa6cf"></span>
    <span class="insurer" style="background:#9ac0e0"></span>
  </div>

  <p class="abs transport">FREE TRANSPORT ASSISTANCE AVAILABLE</p>
  <div class="site" style="top:662px">
    <svg width="9" height="12" viewBox="0 0 9 12"><path d="M4.5 0 A4.5 4.5 0 0 1 9 4.5 C9 7.5 4.5 12 4.5 12 C4.5 12 0 7.5 0 4.5 A4.5 4.5 0 0 1 4.5 0 Z" fill="var(--navy)"/><circle cx="4.5" cy="4.5" r="1.8" fill="#fff"/></svg>
    <div><p class="site-name">MORVAL CARE BURLINGTON, KENTUCKY</p><p class="site-address">4200 Commerce Pkwy, Burlington, KY 41005</p></div>
  </div>
  <div class="site" style="top:694px">
    <svg width="9" height="12" viewBox="0 0 9 12"><path d="M4.5 0 A4.5 4.5 0 0 1 9 4.5 C9 7.5 4.5 12 4.5 12 C4.5 12 0 7.5 0 4.5 A4.5 4.5 0 0 1 4.5 0 Z" fill="var(--navy)"/><circle cx="4.5" cy="4.5" r="1.8" fill="#fff"/></svg>
    <div><p class="site-name">MORVAL CARE RICHMOND, KENTUCKY</p><p class="site-address">1850 Meadow Ridge Dr, Richmond, KY 40475</p></div>
  </div>
  <p class="contact-item" style="left:307px;top:730px"><svg width="10" height="10" viewBox="0 0 14 14"><circle cx="7" cy="7" r="7" fill="var(--navy)"/><path d="M4.5 3.5 L6 5.5 L5.2 6.5 C5.8 7.7 6.5 8.4 7.5 8.8 L8.5 8 L10.5 9.5 L9.7 10.7 C7 10.5 3.6 7 3.3 4.3 Z" fill="#fff"/></svg>859-555-0142</p>
  <p class="contact-item" style="left:403px;top:730px"><svg width="10" height="10" viewBox="0 0 14 14"><circle cx="7" cy="7" r="6" fill="none" stroke="var(--navy)" stroke-width="2"/><path d="M1 7 H13 M7 1 C4 4 4 10 7 13 M7 1 C10 4 10 10 7 13" fill="none" stroke="var(--navy)" stroke-width="1.2"/></svg>morvalcare.org</p>
</div>
</section>

</body>
</html>
```